Business Card Design Project

Hello- I am an interior stylist/product designer whose work is detail driven, very clean and transitional in style and I want my business card to reflect those qualities. I have a logo that I use on my website- my name and a hand drawn chandelier that I want incorporated into the design. However, "Design for the Home" needs to be changed to "Designs". I will be using cream colored stock and am thinking of gray text and logo. I need your help in pulling my card together since it will be the most used element and drive the design of the rest of my stationary suite.
Updates

Please note that I have changed my QR code from my cell # to my website. The new code will be downloaded now.

Reason: I want to thank everyone who has submitted designs- there are truly some very inspiring designs and I am very pleased. I want to make certain that I get this right and have an attractive and highly effective marketing tool when we are finished. With that said, I have run into a technical problem with one aspect of the card- a qr code for my website that was not part of the original brief. I will get that corrected today and post. Once I get that taken care of, I will post comments to all designs received do far. Thanks again for everyone's efforts, Risa

QR Code for the website is now uploaded. Thanks for your patience!

Target Market(s)

Upper middle class- mostly women

Industry/Entity Type

Business

Requirements
Must have
• Marisa Vantry Designs
"...to the last detail."
214-555-0148
marisavantry@plumwick.net
www.marisavantrydesigns-example.com
27083 Birchmont Court
Dallas, TX 75000
Nice to have
• Risa Vantry
Owner

```html
<!DOCTYPE html>
<html lang="en">
<head>
<meta charset="utf-8">
<title>Marisa Vantry Designs — Business Card</title>
<link rel="stylesheet" href="https://fonts.googleapis.com/css2?family=Lora:ital,wght@0,400;1,700&display=swap">
<style>
  :root {
    --card-bg: #ffffff;
    --rule-dark: #6a6a6a;
    --rule-light: #a9a9a9;
    --wordmark: #666666;
    --tagline: #a3a3a3;
    --contact: #8c8c8c;
  }
  html, body {
    margin: 0;
    padding: 0;
    overflow: hidden;
    background: var(--card-bg);
  }
  .card {
    position: relative;
    width: 1200px;
    height: 734px;
    background: var(--card-bg);
    overflow: hidden;
    font-family: "Lora", Georgia, serif;
  }
  .rule { position: absolute; }
  .rule--vertical { width: 3px; background: var(--rule-dark); }
  .rule--horizontal { height: 4px; background: var(--rule-light); }
  .rule--left   { left: 137px;  top: 99px;  height: 597px; }
  .rule--right  { left: 1072px; top: 27px;  height: 595px; }
  .rule--top    { top: 111px; left: 348px; width: 811px; }
  .rule--bottom { top: 606px; left: 54px;  width: 812px; }

  .wordmark {
    position: absolute;
    left: 325px;
    top: 228px;
    width: 582px;
    text-align: center;
    color: var(--wordmark);
    font-weight: 400;
  }
  .wordmark__name {
    display: block;
    font-size: 66px;
    line-height: 1;
  }
  .wordmark__sub {
    display: block;
    margin-top: 20px;
    font-size: 21px;
    letter-spacing: 5px;
    line-height: 1;
  }
  .tagline {
    position: absolute;
    left: 0;
    top: 380px;
    width: 1232px;
    margin: 0;
    text-align: center;
    font-style: italic;
    font-weight: 700;
    font-size: 50px;
    line-height: 1;
    color: var(--tagline);
  }
  .contact {
    position: absolute;
    left: 156px;
    top: 487px;
    margin: 0;
    font-style: normal;
    font-size: 20px;
    line-height: 28.5px;
    color: var(--contact);
  }
  .contact span { display: block; }
  .website {
    position: absolute;
    right: 190px;
    top: 572px;
    font-size: 20px;
    line-height: 1;
    color: var(--contact);
  }
</style>
</head>
<body>
  <main class="card">
    <div class="rule rule--vertical rule--left"></div>
    <div class="rule rule--vertical rule--right"></div>
    <div class="rule rule--horizontal rule--top"></div>
    <div class="rule rule--horizontal rule--bottom"></div>

    <h1 class="wordmark">
      <span class="wordmark__name">Marisa Vantry</span>
      <span class="wordmark__sub">DESIGNS</span>
    </h1>

    <p class="tagline">“...to the last detail.”</p>

    <address class="contact">
      <span>214-555-0148</span>
      <span>marisavantry@plumwick.net</span>
      <span>27083 Birchmont Court</span>
      <span>Dallas, TX 75000</span>
    </address>

    <div class="website">www.marisavantrydesigns-example.com</div>
  </main>
</body>
</html>
```